Business Card Design

We sell fish products to corporate food companies who then turn these products into final food products for consumers

Industry/Entity Type

Business

Contact Information for Business Card

I need a corporate business card template for a fish products business. We would like it be professional for use in dealing with multi national companies. This company business card template will be used by multiple employees so the following fields must be open to edit (Name, Phone Number and Email address)

```html
<!DOCTYPE html>
<html lang="en">
<head>
<meta charset="UTF-8">
<title>Coral Bay Fishery – Business Card</title>
<link rel="stylesheet" href="https://fonts.googleapis.com/css2?family=Tinos&display=swap">
<style>
  :root {
    --page-bg: #e6e8ea;
    --card-white: #efefef;
    --blue-deep: #0866b8;
    --blue-main: #1690d6;
    --blue-bright: #2aaae2;
    --blue-light: #6cc6ec;
    --ink-brand: #2b4f9c;
    --ink-field: #5a5a96;
    --dots: #8a8aa8;
  }
  * { box-sizing: border-box; margin: 0; padding: 0; }
  html, body {
    width: 1200px;
    height: 754px;
    overflow: hidden;
    background: var(--page-bg);
  }
  .business-card {
    position: absolute;
    left: 170px;
    top: 124px;
    width: 860px;
    height: 505px;
    background: var(--card-white);
    overflow: hidden;
    box-shadow: 0 6px 24px rgba(0, 0, 0, 0.18);
    font-family: "Tinos", "Times New Roman", serif;
  }
  .card-facets {
    position: absolute;
    inset: 0;
    width: 100%;
    height: 100%;
  }
  .brand-name {
    position: absolute;
    left: 46px;
    top: 150px;
    color: var(--ink-brand);
    font-weight: 400;
    text-align: center;
    line-height: 1;
  }
  .brand-name .brand-line-main {
    display: block;
    font-size: 50px;
    letter-spacing: 0.5px;
  }
  .brand-name .brand-line-sub {
    display: block;
    margin-top: 6px;
    font-size: 28px;
    letter-spacing: 7px;
  }
  .contact-fields {
    position: absolute;
    left: 417px;
    top: 252px;
    width: 400px;
    list-style: none;
  }
  .contact-field {
    display: flex;
    align-items: baseline;
    height: 64px;
    color: var(--ink-field);
    font-size: 23px;
  }
  .field-label { width: 112px; }
  .field-colon { width: 16px; }
  .field-blank {
    flex: 1;
    border-bottom: 2px dotted var(--dots);
    height: 18px;
  }
</style>
</head>
<body>
  <div class="business-card">
    <svg class="card-facets" viewBox="0 0 542 318" preserveAspectRatio="none" aria-hidden="true">
      <defs>
        <linearGradient id="blue-panel" x1="0" y1="0" x2="1" y2="1">
          <stop offset="0" stop-color="#0a6cbc"/>
          <stop offset="0.6" stop-color="#1a96d8"/>
          <stop offset="1" stop-color="#23a6e0"/>
        </linearGradient>
      </defs>
      <polygon points="0,0 385,0 188,237 328,318 0,318" fill="url(#blue-panel)"/>
      <polygon points="322,0 385,0 188,237 150,212" fill="#5bbbe8" opacity="0.45"/>
      <polygon points="188,237 328,318 255,318" fill="#6cc6ec" opacity="0.8"/>
      <polygon points="140,180 188,237 255,318 150,318" fill="#2aaae2" opacity="0.55"/>
      <polygon points="0,205 130,318 0,318" fill="#0866b8" opacity="0.7"/>
      <polygon points="385,0 400,0 202,245 188,237" fill="#ffffff" opacity="0.35"/>
    </svg>

    <h1 class="brand-name">
      <span class="brand-line-main">CORAL BAY</span>
      <span class="brand-line-sub">FISHERY</span>
    </h1>

    <ul class="contact-fields">
      <li class="contact-field"><span class="field-label">Name</span><span class="field-colon">:</span><span class="field-blank"></span></li>
      <li class="contact-field"><span class="field-label">Phone</span><span class="field-colon">:</span><span class="field-blank"></span></li>
      <li class="contact-field"><span class="field-label">E-Mail</span><span class="field-colon">:</span><span class="field-blank"></span></li>
    </ul>
  </div>
</body>
</html>
```